Business card design for IT consulting company

Looking for a simple, modern, clean business card design.
Open to reworking our existing logo.

Attached is our current business cards which we do not like.
Ideally double sided with something simple on the back.
Rectangle / Horizonal only.
No rounded edges on the card.
White as the dominate color is preferred.

Target Market(s)

clients, legal, oil & gas, medical, professionals

Industry/Entity Type

IT, tech, consulting

Contact Information for Business Card

Name, Title, email, phone, cell, website

Font styles to use
Sans Serif

Requirements
Must have
• Clean design
Should not have
• loud colors or unusual fonts, etc

```html
<!DOCTYPE html>
<html lang="en">
<head>
<meta charset="utf-8">
<title>Norvex Solutions – Business Card</title>
<link href="https://fonts.googleapis.com/css2?family=Raleway:wght@400;800&family=Open+Sans:wght@400&display=swap" rel="stylesheet">
<style>
  :root {
    --stage: #d9d9d9;
    --paper: #ffffff;
    --ink: #0a0cae;
    --night: #0b0f12;
    --pattern: #14191d;
    --sun: #fdc21f;
    --sky: #5ce0fc;
    --rose: #ff2568;
    --navy: #000bb0;
    --white: #ffffff;
  }
  * { margin: 0; padding: 0; box-sizing: border-box; }
  html, body { width: 1200px; height: 846px; overflow: hidden; }
  body { background: var(--stage); position: relative; font-family: "Open Sans", Arial, sans-serif; }

  .card { position: absolute; left: 347px; width: 509px; height: 291px; overflow: hidden; }
  .card--front { top: 99px; background: var(--paper); }
  .card--back { top: 457px; background: var(--night); }

  .brand-block {
    position: absolute; left: 101px; top: 71px; width: 148px; height: 148px;
    display: flex; align-items: center; justify-content: center; gap: 8px;
  }
  .brand-square { width: 16px; height: 16px; background: var(--ink); }
  .brand-name {
    font-family: "Raleway", Arial, sans-serif; font-weight: 800;
    font-size: 30px; color: var(--ink); letter-spacing: -0.5px;
  }

  .person { position: absolute; left: 268px; top: 64px; color: var(--ink); }
  .person-name {
    font-family: "Raleway", Arial, sans-serif; font-weight: 800;
    font-size: 24px; line-height: 28px; letter-spacing: -0.3px;
  }
  .person-title {
    font-family: "Raleway", Arial, sans-serif; font-weight: 400;
    font-size: 16px; line-height: 20px;
  }

  .contacts { position: absolute; left: 268px; top: 122px; list-style: none; color: var(--ink); }
  .contact { display: flex; align-items: center; height: 25px; font-size: 16px; }
  .contact svg { width: 16px; height: 16px; margin-right: 7px; fill: var(--ink); flex: none; }

  .stripe { position: absolute; left: 0; bottom: 0; width: 100%; height: 10px; display: flex; }
  .stripe span { flex: 1; }
  .stripe .sun { background: var(--sun); }
  .stripe .sky { background: var(--sky); }
  .stripe .rose { background: var(--rose); }
  .stripe .navy { background: var(--navy); }

  .back-pattern { position: absolute; inset: 0; background: linear-gradient(180deg, var(--pattern), var(--night)); }
  .back-brand {
    position: absolute; left: 233px; top: 182px; height: 42px;
    display: flex; align-items: center; gap: 8px;
  }
  .back-brand .brand-square { width: 14px; height: 14px; background: var(--white); }
  .back-brand .brand-name { color: var(--white); font-size: 25px; font-weight: 800; letter-spacing: 0; }
</style>
</head>
<body>
  <section class="card card--front">
    <div class="brand-block">
      <span class="brand-square"></span>
      <span class="brand-name">Norvex</span>
    </div>

    <div class="person">
      <div class="person-name">Daniel Reyes</div>
      <div class="person-title">IT Consultant</div>
    </div>

    <ul class="contacts">
      <li class="contact">
        <svg viewBox="0 0 16 16"><path d="M1 4h14v9H1z M1 4l7 5 7-5" fill="none" stroke="currentColor"/><path d="M1 4h14L8 9z"/><path d="M1 5v8h14V5L8 10z"/></svg>
        daniel.reyes@norvex.ca
      </li>
      <li class="contact">
        <svg viewBox="0 0 16 16"><path d="M3.5 1.5l2.5 3-1.5 1.8c.8 1.8 2.3 3.3 4.2 4.2L10.5 9l3 2.5-1.3 2.7C6.5 14 2 9.5 1.8 3z"/></svg>
        (888) 555-0142
      </li>
      <li class="contact">
        <svg viewBox="0 0 16 16"><path d="M4.5 1h7a1 1 0 0 1 1 1v12a1 1 0 0 1-1 1h-7a1 1 0 0 1-1-1V2a1 1 0 0 1 1-1zm.5 2v9h6V3zm3 9.7a.8.8 0 1 0 0 1.6.8.8 0 0 0 0-1.6z"/></svg>
        (604) 555-0187
      </li>
      <li class="contact">
        <svg viewBox="0 0 16 16"><g fill="none" stroke="#0a0cae" stroke-width="1"><circle cx="8" cy="8" r="6.5"/><ellipse cx="8" cy="8" rx="3" ry="6.5"/><path d="M1.5 8h13M2.5 5h11M2.5 11h11M8 1.5v13"/></g></svg>
        www.norvex.ca
      </li>
    </ul>

    <div class="stripe">
      <span class="sun"></span><span class="sky"></span><span class="rose"></span><span class="navy"></span>
    </div>
  </section>

  <section class="card card--back">
    <div class="back-pattern" role="img" aria-label="Faint repeating pattern of the company name across the dark card back"></div>
    <div class="back-brand">
      <span class="brand-square"></span>
      <span class="brand-name">Norvex Solutions</span>
    </div>
  </section>
</body>
</html>
```